Important Solar Energy Company Needs a Stationery Design

I need a modern, attractive, corporate stationary design (letter head and business card)
Attached Company Logo

Target Market(s)

Upmarket

Industry/Entity Type

Business

Colors
ec1f27
ffffff
757575
cbcbcb
000000

```html
<!DOCTYPE html>
<html lang="it">
<head>
<meta charset="utf-8">
<title>SolareVivo — Business Card</title>
<link rel="stylesheet" href="https://fonts.googleapis.com/css2?family=Lato:ital,wght@0,300;0,400;0,700;1,300&display=swap">
<style>
  :root {
    --brand-red: #ec1f27;
    --paper: #ffffff;
    --text-grey: #757575;
    --backdrop: #cbcbcb;
    --ink: #000000;
    --ink-soft: #3a3a3a;
  }
  * { margin: 0; padding: 0; box-sizing: border-box; }
  html, body {
    width: 1200px; height: 1000px; overflow: hidden;
    background: var(--backdrop);
    font-family: "Lato", sans-serif;
  }
  .sheet {
    position: relative; width: 1200px; height: 1000px;
  }
  .card {
    position: absolute; width: 580px; height: 350px;
    box-shadow: 0 4px 14px rgba(0,0,0,0.18);
  }
  .card--front { left: 310px; top: 110px; background: var(--brand-red); }
  .card--back { left: 310px; top: 540px; background: var(--paper); }

  .brand {
    position: absolute; display: flex; flex-direction: column; align-items: center; gap: 10px;
  }
  .brand__dot { width: 58px; height: 58px; border-radius: 50%; }
  .brand__name { font-weight: 400; letter-spacing: 2px; font-size: 17px; }

  .card--front .brand { right: 70px; top: 120px; }
  .card--front .brand__dot { background: var(--paper); }
  .card--front .brand__name { color: var(--paper); }

  .card--back .brand { right: 40px; top: 36px; }
  .card--back .brand__dot { background: var(--brand-red); width: 48px; height: 48px; }
  .card--back .brand__name { color: var(--ink-soft); font-size: 14px; }

  .holder { position: absolute; left: 44px; top: 150px; }
  .holder__name { font-weight: 300; font-size: 24px; color: var(--ink-soft); }
  .holder__role { font-weight: 300; font-size: 20px; color: var(--brand-red); margin-top: 4px; }

  .address {
    position: absolute; left: 44px; bottom: 40px;
    font-weight: 300; font-size: 16px; line-height: 1.35; color: var(--text-grey);
  }

  .contacts {
    position: absolute; right: 40px; top: 150px;
    font-size: 13px; line-height: 1.45; color: var(--text-grey); font-weight: 300;
  }
  .contacts dt { display: inline; color: var(--brand-red); font-weight: 700; }
  .contacts dd { display: inline; }
  .contacts dd::after { content: ""; display: block; }
</style>
</head>
<body>
<main class="sheet">
  <section class="card card--front" aria-label="Card front">
    <div class="brand">
      <span class="brand__dot"></span>
      <span class="brand__name">SOLAREVIVO</span>
    </div>
  </section>

  <section class="card card--back" aria-label="Card back">
    <div class="brand">
      <span class="brand__dot"></span>
      <span class="brand__name">SOLAREVIVO</span>
    </div>

    <div class="holder">
      <p class="holder__name">Marco Bellini Ruiz</p>
      <p class="holder__role">Managing Director</p>
    </div>

    <dl class="contacts">
      <dt>Tel:</dt> <dd>+39.0861.555.2100</dd>
      <dt>Fax:</dt> <dd>+39.0861.555.2102</dd>
      <dt>Web:</dt> <dd>www.solarevivo.it</dd>
      <dt>Email:</dt> <dd>hello@solarevivo.it</dd>
    </dl>

    <address class="address" style="font-style:normal">
      Via Lungomare, 58<br>
      64025-Pineto Marina TE
    </address>
  </section>
</main>
</body>
</html>
```